Kestrel Bathrooms

Fix our flyer add as the one we got made has the wrong phone number on it would like different photos on it

Want it to Stand out and be in your face!

I will attach our logo
phone number is 0487265903
Email is Miles@kestrelbathrooms.com.au

happy to keep all prices the same

If you can make it better happy to tip $$

```html
<!DOCTYPE html>
<html lang="en">
<head>
<meta charset="UTF-8">
<title>Kestrel Bathrooms – Flyer</title>
<link rel="stylesheet" href="https://fonts.googleapis.com/css2?family=Poppins:ital,wght@0,400;0,500;0,600;0,700;0,800;1,500;1,600;1,700;1,800;1,900&display=swap">
<style>
  :root {
    --blue: #1e6ac8;
    --blue-deep: #2453b8;
    --black: #0b0b0b;
    --white: #ffffff;
    --grey: #d9d9d9;
    --page: #e6e6e6;
    --ink: #111111;
  }
  * { margin: 0; padding: 0; box-sizing: border-box; }
  html, body { width: 1200px; height: 678px; overflow: hidden; }
  body { background: var(--page); font-family: "Poppins", sans-serif; }

  .flyer {
    position: absolute; left: 360px; top: 0;
    width: 480px; height: 678px;
    background: var(--white); overflow: hidden;
  }
  .flyer-shapes { position: absolute; inset: 0; }
  .abs { position: absolute; }

  .brand {
    left: 22px; top: 44px; display: flex; align-items: center; gap: 10px;
    color: var(--blue); font-weight: 600; font-size: 26px; letter-spacing: 0.5px;
    line-height: 1;
  }
  .brand-mark { width: 22px; height: 22px; background: var(--blue); }

  .headline {
    left: 20px; top: 136px;
    font-weight: 900; font-style: italic; font-size: 39px;
    line-height: 34px; letter-spacing: -1.2px; text-transform: uppercase;
  }
  .headline .blue { color: var(--blue); display: block; }
  .headline .dark { color: var(--ink); display: block; }

  .package {
    left: 21px; width: 222px; height: 100px;
    background: linear-gradient(90deg, #e9e9e9 45%, #ffffff 100%);
  }
  .package-photo {
    position: absolute; left: 0; top: 0; width: 100px; height: 100px;
    border: 3px solid var(--black);
  }
  .package-save {
    position: absolute; left: 65px; top: 65px; width: 35px; height: 35px;
    background: var(--blue); color: var(--white);
    font-size: 7px; font-weight: 700; line-height: 7px; text-align: center;
    display: flex; flex-direction: column; justify-content: center;
  }
  .package-title {
    position: absolute; left: 105px; top: 12px;
    color: var(--blue); font-weight: 700; font-size: 16px; line-height: 14px;
    text-transform: uppercase;
  }
  .package-rule {
    position: absolute; left: 104px; right: 26px; top: 64px;
    height: 1px; background: var(--blue);
  }
  .package-from {
    position: absolute; left: 105px; top: 70px;
    font-size: 6.5px; font-weight: 600; color: var(--ink);
  }
  .package-price {
    position: absolute; left: 104px; top: 76px;
    font-size: 15px; font-weight: 900; font-style: italic; color: var(--ink);
  }

  .tagline {
    right: 20px; top: 227px; text-align: right;
    color: var(--white); font-weight: 600; font-size: 12.5px; line-height: 13px;
    text-transform: uppercase;
  }
  .built {
    left: 275px; top: 314px;
    color: var(--white); font-weight: 700; font-size: 26px; line-height: 23px;
    text-transform: uppercase;
  }
  .specialist {
    left: 275px; top: 365px;
    color: var(--white); font-size: 9.5px; font-weight: 500;
  }

  .services { left: 275px; top: 382px; width: 190px; list-style: none; }
  .service {
    display: flex; align-items: center; gap: 11px; height: 25.7px;
    border-bottom: 1px solid rgba(255,255,255,0.35);
    color: var(--white); font-style: italic; font-weight: 600; font-size: 11px;
  }
  .service:last-child { border-bottom: none; }
  .service svg { width: 16px; height: 16px; flex: none; }

  .fixtures {
    left: 275px; top: 565px;
    color: var(--white); font-size: 9.5px; font-weight: 400;
  }
  .terms {
    left: 0; width: 480px; top: 591px; text-align: center;
    font-size: 9.5px; font-style: italic; font-weight: 500; color: var(--ink);
  }

  .call { left: 22px; top: 625px; display: flex; align-items: center; gap: 10px; color: var(--white); }
  .call-label { font-size: 10.5px; font-weight: 600; line-height: 10px; }
  .call-number { font-size: 25px; font-weight: 800; line-height: 25px; letter-spacing: -0.3px; }
  .contact { left: 250px; top: 635px; display: flex; align-items: center; gap: 10px; color: var(--white); }
  .contact-lines { font-size: 10px; font-weight: 700; line-height: 12px; }
</style>
</head>
<body>
<main class="flyer">
  <svg class="flyer-shapes" width="480" height="678" viewBox="0 0 480 678" aria-hidden="true">
    <defs>
      <linearGradient id="panelBlue" x1="0" y1="0" x2="0" y2="1">
        <stop offset="0" stop-color="#1e6ac8"/>
        <stop offset="1" stop-color="#2a4fb7"/>
      </linearGradient>
      <linearGradient id="roomTones" x1="0" y1="0" x2="1" y2="1">
        <stop offset="0" stop-color="#c89a4a"/>
        <stop offset="0.4" stop-color="#8a6e60"/>
        <stop offset="1" stop-color="#5b5f78"/>
      </linearGradient>
    </defs>
    <!-- header band -->
    <rect x="0" y="0" width="480" height="122" fill="var(--black)"/>
    <!-- blue service panel -->
    <rect x="261" y="205" width="219" height="382" fill="url(#panelBlue)"/>
    <!-- framed hero diamond -->
    <polygon points="200,120 410,-90 620,120 410,330" fill="var(--grey)"/>
    <polygon points="222,120 410,-68 598,120 410,308" fill="var(--white)"/>
    <!-- tagline tab -->
    <polygon points="263,217 480,217 480,266 290,266 263,244" fill="var(--black)"/>
    <!-- specialist strip -->
    <rect x="261" y="365" width="219" height="13" fill="var(--black)"/>
    <!-- footer -->
    <rect x="0" y="610" width="480" height="68" fill="var(--black)"/>
    <polygon points="0,610 260,610 215,678 0,678" fill="var(--blue-deep)"/>
  </svg>

  <svg class="abs" style="left:0;top:0" width="480" height="330" viewBox="0 0 480 330" role="img" aria-label="Overhead photo of a finished bathroom with brick wall, vanity basin and toilet">
    <polygon points="232,120 410,-58 588,120 410,298" fill="url(#roomTones)"/>
  </svg>

  <div class="abs brand"><span class="brand-mark"></span>Kestrel Bathrooms</div>

  <h1 class="abs headline"><span class="blue">Fully</span><span class="blue">Licensed</span><span class="dark">&amp; Insured</span></h1>

  <article class="abs package" style="top:259px">
    <div class="package-photo" role="img" aria-label="Photo of a vanity basin against green tiles" style="background:linear-gradient(135deg,#2f4a3a,#6f7a6a 60%,#d8d4cc)"></div>
    <div class="package-save"><span>SAVE UP</span><span>TO</span><span>$4,000</span></div>
    <h2 class="package-title">Main<br>Bathroom<br>Package</h2>
    <div class="package-rule"></div>
    <p class="package-from">Price Starts From</p>
    <p class="package-price">$18,900</p>
  </article>

  <article class="abs package" style="top:372px">
    <div class="package-photo" role="img" aria-label="Photo of an ensuite with freestanding bath by a window" style="background:linear-gradient(135deg,#3a3532,#9a948c 55%,#e8e6e2)"></div>
    <div class="package-save"><span>SAVE UP</span><span>TO</span><span>$4,000</span></div>
    <h2 class="package-title" style="top:20px">Ensuite<br>Package</h2>
    <div class="package-rule"></div>
    <p class="package-from">Price Starts From</p>
    <p class="package-price">$14,900</p>
  </article>

  <article class="abs package" style="top:485px">
    <div class="package-photo" role="img" aria-label="Photo of a laundry with washing machine and stone benchtop basin" style="background:linear-gradient(135deg,#6c6a68,#c9b8a0 55%,#eeeae4)"></div>
    <div class="package-save"><span>SAVE UP</span><span>TO</span><span>$4,000</span></div>
    <h2 class="package-title" style="top:20px">Laundry<br>Package</h2>
    <div class="package-rule"></div>
    <p class="package-from">Price Starts From</p>
    <p class="package-price">$9,900</p>
  </article>

  <p class="abs tagline">Illawarra based and<br>family operated</p>
  <h2 class="abs built">Built<br>to last</h2>
  <p class="abs specialist">Your local renovation specialist</p>

  <ul class="abs services">
    <li class="service"><svg viewBox="0 0 16 16"><path d="M3 3h10v3H9v8H7V6H3z" fill="#fff"/></svg>Demolition</li>
    <li class="service"><svg viewBox="0 0 16 16"><path d="M9 1L3 9h4l-1 6 6-8H8z" fill="#fff"/></svg>Electrical</li>
    <li class="service"><svg viewBox="0 0 16 16"><path d="M2 12L12 2l2 2L4 14z" fill="#fff"/></svg>Carpentry</li>
    <li class="service"><svg viewBox="0 0 16 16"><rect x="2" y="3" width="12" height="8" fill="none" stroke="#fff" stroke-width="1.5"/><path d="M6 14h4" stroke="#fff" stroke-width="1.5"/></svg>Design Consultation</li>
    <li class="service"><svg viewBox="0 0 16 16"><path d="M8 2C6 5 4.5 7 4.5 9a3.5 3.5 0 0 0 7 0C11.5 7 10 5 8 2z" fill="#fff"/><path d="M2 15h12" stroke="#fff" stroke-width="1.5"/></svg>Waterproofing</li>
    <li class="service"><svg viewBox="0 0 16 16"><path d="M2 4h8v3h3v7h-3V10H2z" fill="#fff"/></svg>Plumbing</li>
    <li class="service"><svg viewBox="0 0 16 16"><rect x="2" y="2" width="5" height="5" fill="#fff"/><rect x="9" y="2" width="5" height="5" fill="#fff"/><rect x="2" y="9" width="5" height="5" fill="#fff"/><rect x="9" y="9" width="5" height="5" fill="#fff"/></svg>Tiling</li>
  </ul>
  <p class="abs fixtures">Organisation and delivery of all fixtures</p>

  <p class="abs terms">*Terms and conditions apply and onsite quote required.</p>

  <div class="abs call">
    <svg width="22" height="22" viewBox="0 0 24 24" aria-hidden="true"><path d="M6.6 2.5l3 3.2-1.8 2.2a12 12 0 0 0 8.3 8.3l2.2-1.8 3.2 3-2 3.1C11 20.5 3.5 13 2.5 4.5z" fill="none" stroke="#fff" stroke-width="1.6" stroke-linejoin="round"/></svg>
    <div><p class="call-label">CALL US AT</p><p class="call-number">0487265903</p></div>
  </div>

  <div class="abs contact">
    <svg width="20" height="20" viewBox="0 0 24 24" aria-hidden="true"><circle cx="12" cy="12" r="10" fill="none" stroke="#fff" stroke-width="1.8"/><ellipse cx="12" cy="12" rx="4.5" ry="10" fill="none" stroke="#fff" stroke-width="1.5"/><path d="M2 12h20M4 7h16M4 17h16" stroke="#fff" stroke-width="1.3"/></svg>
    <div class="contact-lines"><p>www.kestrelbathrooms.com.au</p><p>miles@kestrelbathrooms.com.au</p></div>
  </div>
</main>
</body>
</html>
```